bramblewood mental health web page

this is to be a single page with no links - will function just like an add.
will have 2 biographies
contact info.
Updates

Dear Designers - most of these are too complex.

 Just want one page with contact details (yet to be sorted). No email contact as we can't monitor all emails and if person emails saying suicidal I am potentially accountable if they are successful. Hence- this is just like a listing in a phone book. 
2 photos - one of me the other my husband - with a little blurb next to our names.
No info on fees or appointments etc
I am legally not allowed use language like - "what sets us apart" - it suggests we are better than other clinicians and that is illegal. 
NO EMOTIVE PHOTOS PLEASE! 

Target Market(s)

clients wanting check background and contact information.

Industry/Entity Type

Mental Health

Requirements
Must have
• NEW LOGO
space for photographs
Old web page to complicated
http://wbtk.net.au/index.shtml
Should not have
• anything that flashes.

```html
<!DOCTYPE html>
<html lang="en">
<head>
<meta charset="utf-8">
<title>Bramblewood Mental Health</title>
<link href="https://fonts.googleapis.com/css2?family=Roboto:wght@300;400&family=Open+Sans:wght@400;600;700&display=swap" rel="stylesheet">
<style>
:root{
  --navy:#1b2a6b;
  --teal:#1fa9c2;
  --teal-soft:#bfe2e4;
  --grey-bg:#f2f2f2;
  --text:#333;
  --muted:#555;
  --rule:#e1e1e1;
  --arrow:#2a8fc0;
  --tick:#3c9a3c;
}
*{margin:0;padding:0;box-sizing:border-box}
html,body{width:902px;height:1200px;overflow:hidden}
body{position:relative;background:#e8f3f4;font-family:"Open Sans",sans-serif;color:var(--text)}
.top-strip{position:absolute;left:0;top:0;width:902px;height:8px;background:var(--teal)}
.site-header{position:absolute;left:0;top:8px;width:902px;height:72px;background:var(--grey-bg)}
.brand{position:absolute;left:106px;top:8px;display:flex;align-items:center;gap:10px}
.brand-square{width:48px;height:48px;background:var(--navy)}
.brand-name{font-family:"Roboto",sans-serif;font-weight:300;font-size:19px;line-height:22px;color:var(--navy);width:150px}
.header-divider{position:absolute;left:338px;top:8px;width:1px;height:58px;background:#d8d8d8}
.tagline{position:absolute;left:354px;top:14px;font-family:"Roboto",sans-serif;font-weight:300;font-size:19px;line-height:21px;color:var(--navy)}
.contact{position:absolute;left:592px;top:13px;font-size:10px;line-height:21px;color:var(--text)}
.contact .row{display:flex;align-items:center;gap:6px}
.contact .label{color:var(--navy)}
.contact .ids{font-size:8px;color:var(--muted);padding-left:44px;line-height:12px;margin-top:2px}
.hero{position:absolute;left:0;top:80px;width:902px;height:282px;background:var(--teal-soft)}
.hero-figure{position:absolute;left:104px;top:16px;width:264px;height:266px;border-radius:130px 130px 20px 20px;background:radial-gradient(circle at 50% 40%,#7d9496,#bfe2e4 75%)}
.hero-text{position:absolute;left:388px;top:60px;width:420px;font-family:"Roboto",sans-serif;color:#1a1a2e}
.hero-text h1{font-weight:400;font-size:26px;color:var(--navy);margin-bottom:4px}
.hero-text p{font-size:18px;line-height:31.8px}
.clinician{position:absolute;left:106px;width:690px;height:318px;background:#fff;border:1px solid #d5d5d5}
.clinician.first{top:376px}
.clinician.second{top:709px}
.portrait{position:absolute;left:8px;top:8px;width:147px;height:161px;border:3px solid var(--teal);background:linear-gradient(160deg,#8a7a6c,#d9cfc6)}
.clinician-name{position:absolute;left:9px;top:174px;font-size:11.5px;line-height:16px;color:var(--navy)}
.clinician-name strong{font-weight:700}
.clinician-name .quals{font-size:10px}
.sec-head{position:absolute;font-size:10px;font-weight:700;color:var(--navy)}
.sec-rule{position:absolute;height:1px;background:var(--rule)}
.ticks{position:absolute;left:172px;top:30px;display:flex;gap:40px;font-size:10.5px}
.ticks span{display:flex;align-items:center;gap:3px}
.list{position:absolute;list-style:none;font-size:10px}
.list li{position:relative;padding-left:14px;line-height:16px}
.list li::before{content:"";position:absolute;left:1px;top:4px;border-left:6px solid var(--arrow);border-top:4px solid transparent;border-bottom:4px solid transparent}
.list li.sub{padding-left:24px;font-size:9px;line-height:13px;color:var(--muted)}
.list li.sub::before{display:none}
.age-groups{position:absolute;left:479px;top:276px;display:grid;grid-template-columns:71px 80px;font-size:9px;line-height:13px;color:var(--muted)}
.gallery{position:absolute;left:0;top:1042px;width:902px;height:102px}
.thumb{position:absolute;top:0;width:109px;height:102px;border:2px solid #fff;outline:1px solid #c8c8c8;border-radius:3px}
.arrow-btn{position:absolute;top:41px;width:19px;height:19px;border-radius:50%;background:#222}
.site-footer{position:absolute;left:0;top:1166px;width:902px;height:34px;background:var(--teal);color:#fff;font-size:9px;text-align:center;line-height:34px}
</style>
</head>
<body>
<div class="top-strip"></div>
<header class="site-header">
  <div class="brand"><div class="brand-square"></div><div class="brand-name">BRAMBLEWOOD MENTAL HEALTH</div></div>
  <div class="header-divider"></div>
  <div class="tagline">Clinical Pyschology &amp;<br>Counselling</div>
  <div class="contact">
    <div class="row"><svg width="10" height="12" viewBox="0 0 10 12"><path d="M5 0a4 4 0 0 0-4 4c0 3 4 8 4 8s4-5 4-8a4 4 0 0 0-4-4zm0 5.5a1.5 1.5 0 1 1 0-3 1.5 1.5 0 0 1 0 3z" fill="#555"/></svg><span><span class="label">Address:</span> 24 Larkspur Court, HALLOWAY 6031</span></div>
    <div class="row"><svg width="10" height="12" viewBox="0 0 10 12"><path d="M2 0l2 3-1 1.5c.6 1.6 1.7 3 3 3.8L7.5 7l2.5 2-1.5 2.5C5 11 1 7 .5 2z" fill="#555"/></svg><span><span class="label">Phone:</span> ( 08) 9300 4718 &nbsp;or 0400 618 295</span></div>
    <div class="ids">ABN: 41 802 356 917 &nbsp;&nbsp;ACN: 208415736</div>
  </div>
</header>

<section class="hero">
  <div class="hero-figure" role="img" aria-label="Illustration of a human head and shoulders made of connected network nodes"></div>
  <div class="hero-text">
    <h1>Bramblewood clinicians</h1>
    <p>have expertise in organisation, clinical psychology, counselling, medicolegal and rehabilitation fields. We are an independent Australian enterprise with no religious, private hospital or other ownership affiliations.</p>
  </div>
</section>

<article class="clinician first">
  <div class="portrait" role="img" aria-label="Portrait photo of clinician seated at a desk"></div>
  <div class="clinician-name"><strong>Helena Marsh R.</strong><br>Psych (Clinical),<br><span class="quals">M. Genetic Couns., B.A. (Psych),</span></div>
  <div class="sec-head" style="left:170px;top:8px">Specialising in the treatment of :</div>
  <div class="sec-rule" style="left:170px;top:24px;width:400px"></div>
  <div class="ticks"><span><svg width="12" height="10" viewBox="0 0 12 10"><path d="M1 5l3 3 7-7" stroke="#3c9a3c" stroke-width="2" fill="none"/></svg>Depression</span><span><svg width="12" height="10" viewBox="0 0 12 10"><path d="M1 5l3 3 7-7" stroke="#3c9a3c" stroke-width="2" fill="none"/></svg>Anxiety</span></div>
  <div class="sec-head" style="left:170px;top:58px">Provider of psychological assessment and therapy for other mental health problems including:</div>
  <ul class="list" style="left:170px;top:83px"><li>Phobias</li><li>Panic</li><li>Adjustment disorder</li><li>Bereavement</li><li>Post-traumatic stress</li><li class="sub">Disorder</li></ul>
  <ul class="list" style="left:311px;top:83px"><li>Eating disorders</li><li>Obsessive</li><li class="sub">Compulsive disorder</li></ul>
  <ul class="list" style="left:459px;top:83px"><li>Bipolar disorder</li><li>Schizophrenia</li><li>Sleep problems</li><li>Personality issues</li></ul>
  <div class="sec-head" style="left:170px;top:185px">Counselling and therapy provided for:</div>
  <div class="sec-head" style="left:459px;top:185px">Other Services :</div>
  <div class="sec-rule" style="left:459px;top:203px;width:185px"></div>
  <ul class="list" style="left:170px;top:211px"><li>Cognitive Assessment</li><li>Neuropsychological</li><li>Assessment</li><li>Memory &amp; Dementia</li><li>Screening</li></ul>
  <ul class="list" style="left:311px;top:211px"><li>Employee Assistance</li><li>Program</li><li>Stress Management</li><li>Medicolegal reports</li></ul>
  <ul class="list" style="left:459px;top:211px"><li>Families</li><li>Couples</li><li>Group</li><li>Individuals</li></ul>
  <div class="age-groups"><span>Children</span><span>Adults</span><span>Adolescents</span><span>Older persons</span></div>
</article>

<article class="clinician second">
  <div class="portrait" role="img" aria-label="Portrait photo of clinician in white coat holding a clipboard" style="background:linear-gradient(160deg,#5fb7b8,#eef2f2)"></div>
  <div class="clinician-name"><strong>Dr Rosalind Kerr</strong><br>Psych (Clinical),<br><span class="quals">M. Genetic Couns., B.A. (Psych),</span></div>
  <div class="sec-head" style="left:170px;top:8px">Specialising in the treatment of :</div>
  <div class="sec-rule" style="left:170px;top:24px;width:400px"></div>
  <div class="ticks"><span><svg width="12" height="10" viewBox="0 0 12 10"><path d="M1 5l3 3 7-7" stroke="#3c9a3c" stroke-width="2" fill="none"/></svg>Depression</span><span><svg width="12" height="10" viewBox="0 0 12 10"><path d="M1 5l3 3 7-7" stroke="#3c9a3c" stroke-width="2" fill="none"/></svg>Anxiety</span></div>
  <div class="sec-head" style="left:170px;top:58px">Provider of psychological assessment and therapy for other mental health problems including:</div>
  <ul class="list" style="left:170px;top:83px"><li>Phobias</li><li>Panic</li><li>Adjustment disorder</li><li>Bereavement</li><li>Post-traumatic stress</li><li class="sub">Disorder</li></ul>
  <ul class="list" style="left:311px;top:83px"><li>Eating disorders</li><li>Obsessive</li><li class="sub">Compulsive disorder</li></ul>
  <ul class="list" style="left:459px;top:83px"><li>Bipolar disorder</li><li>Schizophrenia</li><li>Sleep problems</li><li>Personality issues</li></ul>
  <div class="sec-head" style="left:170px;top:185px">Counselling and therapy provided for:</div>
  <div class="sec-head" style="left:459px;top:185px">Other Services :</div>
  <div class="sec-rule" style="left:459px;top:203px;width:185px"></div>
  <ul class="list" style="left:170px;top:211px"><li>Cognitive Assessment</li><li>Neuropsychological</li><li>Assessment</li><li>Memory &amp; Dementia</li><li>Screening</li></ul>
  <ul class="list" style="left:311px;top:211px"><li>Employee Assistance</li><li>Program</li><li>Stress Management</li><li>Medicolegal reports</li></ul>
  <ul class="list" style="left:459px;top:211px"><li>Families</li><li>Couples</li><li>Group</li><li>Individuals</li></ul>
  <div class="age-groups"><span>Children</span><span>Adults</span><span>Adolescents</span><span>Older persons</span></div>
</article>

<section class="gallery">
  <div class="arrow-btn" style="left:109px"><svg width="19" height="19" viewBox="0 0 19 19"><path d="M11 5l-4 4.5 4 4.5" stroke="#fff" stroke-width="1.8" fill="none"/></svg></div>
  <div class="thumb" style="left:132px;background:linear-gradient(135deg,#222,#9a9a9a)" role="img" aria-label="Black and white photo of a pensive person"></div>
  <div class="thumb" style="left:263px;background:linear-gradient(135deg,#c9a58c,#f0e3d8)" role="img" aria-label="Photo of a person covering their face with a hand"></div>
  <div class="thumb" style="left:394px;background:linear-gradient(135deg,#8f8f96,#e4e4ea)" role="img" aria-label="Photo of a person sitting hunched on the floor"></div>
  <div class="thumb" style="left:525px;background:linear-gradient(90deg,#5a6a78,#c49a7c)" role="img" aria-label="Split photo showing two contrasting expressions"></div>
  <div class="thumb" style="left:656px;background:linear-gradient(135deg,#e8eaf0,#8a6a58)" role="img" aria-label="Photo of a person under a white blanket"></div>
  <div class="arrow-btn" style="left:771px"><svg width="19" height="19" viewBox="0 0 19 19"><path d="M8 5l4 4.5-4 4.5" stroke="#fff" stroke-width="1.8" fill="none"/></svg></div>
</section>

<footer class="site-footer">Copyright © 2014 Bramblewood Mental Health. &nbsp;| &nbsp;All Rights Reserved</footer>
</body>
</html>
```